Textbook cover for dental seminar

I'm looking for a fresh new design for our annual textbook. You will need to incorporate our logo, business name (LoriKSM's Dental Hygiene Academy) - the words "LoriKSM's" needs to be larger or the same size as "Bright Enamel Institute" and colors of dentistry is purple so I like to stick with shades of purple in the design however it does not need to be all purple or only purple. The words "with hygiene career booster" will not be on next years edition so please do not add that. The book will have spiral binding so please account for that when designing. Please see our website for information LoriKSMExamPrep.com

I also want listed on the cover somewhere “The Ultimate Hands-On Exam Review Guide!”

Size will be 8.5" x 11"

```html
<!DOCTYPE html>
<html lang="en">
<head>
<meta charset="UTF-8">
<title>LoriKSM's Bright Enamel Institute — Review Guide Cover</title>
<link rel="stylesheet" href="https://fonts.googleapis.com/css2?family=Bebas+Neue&display=swap">
<style>
  :root {
    --bg-deep: #1d0e3a;
    --bg-mid: #2a1650;
    --wave-violet: #4b2f86;
    --wave-soft: #6a4aa8;
    --badge-purple: #6b3fa0;
    --badge-ring: #8a62c2;
    --text-light: #ffffff;
  }
  * { margin: 0; padding: 0; box-sizing: border-box; }
  html, body {
    width: 927px;
    height: 1200px;
    overflow: hidden;
    background: var(--bg-deep);
  }
  .cover {
    position: relative;
    width: 927px;
    height: 1200px;
    overflow: hidden;
    background: var(--bg-deep);
    font-family: "Bebas Neue", "Oswald", sans-serif;
    color: var(--text-light);
  }
  .cover__waves {
    position: absolute;
    inset: 0;
    width: 927px;
    height: 1200px;
  }
  .cover__title {
    position: absolute;
    top: 52px;
    left: 0;
    width: 100%;
    text-align: center;
    font-weight: 400;
    font-size: 186px;
    line-height: 182px;
    letter-spacing: 4px;
  }
  .cover__tagline {
    position: absolute;
    top: 600px;
    left: 0;
    width: 100%;
    text-align: center;
    font-size: 39px;
    line-height: 46px;
    letter-spacing: 7px;
  }
  .cover__brand {
    position: absolute;
    top: 740px;
    left: 0;
    width: 100%;
    display: flex;
    align-items: center;
    justify-content: center;
    gap: 22px;
  }
  .cover__brand-mark {
    width: 150px;
    height: 150px;
    border-radius: 50%;
    background: var(--badge-purple);
    border: 8px solid var(--badge-ring);
  }
  .cover__brand-name {
    font-size: 40px;
    line-height: 44px;
    letter-spacing: 3px;
    color: var(--text-light);
  }
  .cover__owner {
    position: absolute;
    top: 975px;
    left: 0;
    width: 100%;
    text-align: center;
    font-size: 214px;
    line-height: 214px;
    letter-spacing: 5px;
  }
</style>
</head>
<body>
  <main class="cover">
    <svg class="cover__waves" viewBox="0 0 927 1200" aria-hidden="true">
      <defs>
        <linearGradient id="waveBottomRight" x1="0" y1="0" x2="1" y2="1">
          <stop offset="0" stop-color="#7b3fa6"/>
          <stop offset="1" stop-color="#e0348d"/>
        </linearGradient>
      </defs>
      <path d="M300 0 C420 40 520 10 640 50 C760 90 840 60 927 100 L927 0 Z" fill="var(--bg-mid)"/>
      <path d="M520 0 C620 30 700 60 780 50 C850 40 890 70 927 110 L927 0 Z" fill="var(--wave-violet)" opacity="0.7"/>
      <path d="M0 0 L0 40 C80 20 160 10 260 0 Z" fill="var(--bg-mid)" opacity="0.8"/>
      <path d="M0 1030 C120 1070 230 1110 330 1200 L0 1200 Z" fill="var(--wave-violet)" opacity="0.85"/>
      <path d="M927 860 C820 880 720 960 660 1060 C620 1130 560 1170 480 1200 L927 1200 Z" fill="var(--wave-violet)" opacity="0.75"/>
      <path d="M927 930 C840 960 770 1040 720 1110 C690 1160 640 1190 600 1200 L927 1200 Z" fill="var(--wave-soft)" opacity="0.7"/>
      <path d="M927 990 C860 1020 800 1090 750 1150 C730 1175 700 1195 680 1200 L927 1200 Z" fill="url(#waveBottomRight)"/>
    </svg>

    <h1 class="cover__title">Bright<br>Enamel<br>Institute</h1>

    <p class="cover__tagline">The Ultimate Hands-On Exam<br>Review Guide!</p>

    <div class="cover__brand">
      <span class="cover__brand-mark"></span>
      <span class="cover__brand-name">LoriKSM's Bright<br>Enamel Institute</span>
    </div>

    <p class="cover__owner">LoriKSM's</p>
  </main>
</body>
</html>
```